Use new branding for Florn website

Florn is a medical supplier of fitted socks for patients. Unlike a regular sock you receive upon admission that is slippery and prone to falling, Florn unique factor is it’s gripping material which gives one traction while walking.
We would like to incorporate the new logo and branding into the Florn website. The copy should stay the same. The logos in various formats and brand guidelines are included in the attachments. While the logos have a black or white background, you may use other colors if it integrates well with your design. Please submit your designs in either Wix or Squarespace
Hello all - additional information. We would like the design submission in either Wix or Squarespace.
1 page

```html
<!DOCTYPE html>
<html lang="en">
<head>
<meta charset="utf-8">
<title>Florn Tech</title>
<link href="https://fonts.googleapis.com/css2?family=Montserrat:wght@600;700&family=Roboto:wght@400;500;700&display=swap" rel="stylesheet">
<style>
:root{
  --yellow:#fcc30d;
  --dark:#222222;
  --black:#050505;
  --ink:#1d1d1d;
  --text:#555555;
  --light:#f4f4f4;
  --white:#ffffff;
  --footer:#262626;
  --on-dark:#f2f2f2;
}
*{margin:0;padding:0;box-sizing:border-box}
html,body{width:1200px;height:4069px;overflow:hidden}
body{position:relative;background:var(--white);font-family:"Roboto",sans-serif;color:var(--text)}
.abs{position:absolute}
.h-title{font-family:"Montserrat",sans-serif;font-weight:700;color:var(--ink);letter-spacing:.5px}
.accent{color:var(--yellow)}
.btn{position:absolute;background:var(--yellow);color:var(--ink);font-family:"Roboto",sans-serif;font-weight:700;font-size:14px;display:flex;align-items:center;justify-content:center;letter-spacing:.2px}
.para{font-size:13.5px;line-height:24.5px;text-align:justify}
.para.on-dark{color:var(--on-dark)}
.photo{position:absolute}

.topline{left:0;top:0;width:1200px;height:4px;background:var(--yellow)}
.brand{display:flex;align-items:center;gap:10px;font-family:"Montserrat",sans-serif;font-weight:700;font-size:34px;color:var(--ink);letter-spacing:1px}
.brand-dot{width:28px;height:28px;border-radius:50%;background:var(--yellow)}
.contact-item{display:flex;align-items:center;gap:20px}
.contact-icon{width:50px;height:50px;border-radius:50%;background:var(--yellow);display:flex;align-items:center;justify-content:center}
.contact-label{font-size:13px;font-weight:500;color:#444;margin-bottom:4px}
.contact-value{font-size:20px;font-weight:500;color:var(--ink)}

.nav{left:111px;top:92px;width:978px;height:46px;background:var(--dark);display:flex;align-items:center}
.nav a{color:var(--white);text-decoration:none;font-size:14px;font-weight:700;padding:0 13px;height:46px;display:flex;align-items:center}
.nav a.active{background:var(--yellow);padding:0 17px}
.nav-social{margin-left:auto;display:flex;gap:11px;padding-right:18px}
.nav-social span{width:10px;height:10px;border-radius:50%;background:var(--white)}
.nav-social span:first-child{background:var(--yellow)}

.hero{left:0;top:114px;width:1200px;height:600px;background:linear-gradient(100deg,#8fa0b8 0%,#c9ccd4 35%,#e8e4e2 60%,#d8d4d2 100%)}
.hero-title{left:0;width:1200px;top:352px;text-align:center;color:var(--white);font-size:34px}

.hex-photo{left:111px;top:810px;width:424px;height:483px}
.featured-bg{left:0;top:1391px;width:1200px;height:1336px;background:var(--light)}
.product-title{font-family:"Montserrat",sans-serif;font-weight:700;font-size:24px;color:var(--ink)}
.framed{border:5px solid var(--white);box-shadow:0 0 4px rgba(0,0,0,.08)}

.benefit-photo{left:0;top:2727px;width:600px;height:471px;background:linear-gradient(135deg,#ece8e4 0%,#d9d2cc 45%,#d98b92 80%,#c87a82 100%)}
.benefit-panel{left:600px;top:2727px;width:600px;height:471px;background:var(--black)}

.supplier{position:absolute;top:3356px;width:182px;height:86px;background:var(--white);box-shadow:0 1px 6px rgba(0,0,0,.12);display:flex;align-items:center;justify-content:center}
.supplier span{width:44px;height:44px;border-radius:50%;background:#d7dde3}

.footer{left:0;top:3643px;width:1200px;height:426px;background:var(--footer)}
.newsletter{left:111px;top:3540px;width:978px;height:213px;background:var(--yellow);text-align:center}
.news-title{font-family:"Montserrat",sans-serif;font-weight:700;font-size:36px;color:var(--ink);margin-top:28px}
.news-sub{font-size:16px;color:var(--white);margin-top:10px}
.news-form{position:absolute;left:106px;top:130px;display:flex}
.news-input{width:590px;height:47px;background:var(--white);font-size:14px;color:#666;display:flex;align-items:center;padding-left:17px}
.news-btn{width:175px;height:47px;background:var(--ink);color:var(--white);font-weight:700;font-size:15px;display:flex;align-items:center;justify-content:center}

.foot-brand{font-size:30px;color:var(--white)}
.foot-col h4{font-family:"Roboto",sans-serif;font-weight:500;font-size:20px;color:var(--white);margin-bottom:22px}
.foot-col li{list-style:none;display:flex;align-items:flex-start;gap:14px;font-size:14px;color:#e8e8e8;line-height:18px;margin-bottom:8px}
.foot-col svg{flex:none;margin-top:2px}
.social-round{position:absolute;top:3886px;width:34px;height:34px;border-radius:50%;background:var(--yellow);border:2px solid var(--white)}
.social-round.ghost{background:transparent}
.divider{left:111px;top:4012px;width:978px;height:1px;background:#6a6a6a}
.copyright{left:0;width:1200px;top:4033px;text-align:center;font-size:12.5px;color:#e0e0e0}
</style>
</head>
<body>

<div class="abs topline"></div>

<header>
  <div class="abs brand" style="left:111px;top:26px"><span class="brand-dot"></span>FLORN TECH</div>
  <div class="abs contact-item" style="left:590px;top:26px">
    <div class="contact-icon"><svg width="20" height="20" viewBox="0 0 24 24"><path d="M6.6 10.8a15 15 0 006.6 6.6l2.2-2.2a1 1 0 011-.25 11.4 11.4 0 003.6.57 1 1 0 011 1V20a1 1 0 01-1 1A17 17 0 013 4a1 1 0 011-1h3.5a1 1 0 011 1c0 1.250.2 2.45.57 3.57a1 1 0 01-.25 1z" fill="#1d1d1d"/></svg></div>
    <div><div class="contact-label">CALL US:</div><div class="contact-value">555-014-2738</div></div>
  </div>
  <div class="abs contact-item" style="left:838px;top:26px">
    <div class="contact-icon"><svg width="20" height="16" viewBox="0 0 24 18"><rect x="1" y="1" width="22" height="16" rx="2" fill="#1d1d1d"/><path d="M2 2l10 8 10-8" stroke="#fcc30d" stroke-width="2" fill="none"/></svg></div>
    <div><div class="contact-label">EMAIL US:</div><div class="contact-value">info@florntech.com</div></div>
  </div>
</header>

<section class="abs hero" role="img" aria-label="Photo of a patient sitting on a hospital bed wearing pink grip socks"></section>

<nav class="abs nav">
  <a class="active">HOME</a><a>ABOUT US</a><a>OUR COLLECTIONS</a><a>SUPPLIERS</a><a>BLOG</a><a>CONTACT US</a>
  <div class="nav-social"><span></span><span></span><span></span><span></span></div>
</nav>

<h1 class="abs h-title hero-title">WELCOME TO FLORN TECH</h1>
<div class="btn" style="left:529px;top:417px;width:142px;height:48px">GET STARTED</div>

<svg class="abs hex-photo" viewBox="0 0 424 483" role="img" aria-label="Photo of a nurse fitting socks on an elderly patient">
  <defs><linearGradient id="aboutTone" x1="0" y1="0" x2="1" y2="1"><stop offset="0" stop-color="#e9e4dc"/><stop offset=".55" stop-color="#c9b8a2"/><stop offset="1" stop-color="#6f6a70"/></linearGradient></defs>
  <polygon points="212,0 424,121 424,362 212,483 0,362 0,121" fill="var(--yellow)"/>
  <polygon points="218,4 424,121 424,358 218,476 9,358 9,121" fill="url(#aboutTone)"/>
</svg>
<h2 class="abs h-title" style="left:611px;top:858px;font-size:35px">ABOUT <span class="accent">US</span></h2>
<div class="abs para" style="left:611px;top:925px;width:478px">
  <p>Lorem ipsum dolor sit amet, consectetur adipiscing elit, sed do eiusmod tempor incididunt ut labore et dolore magna aliqua. Ut enim ad minim veniam, quis nostrud exercitation ullamco laboris nisi ut aliquip ex ea commodo consequat. Duis aute irure dolor in reprehenderit in voluptate velit esse cillum dolore eu fugiat nulla pariatura.</p>
  <p style="margin-top:23px">Duis aute irure dolor in reprehenderit in voluptate velit esse cillum dolore eu fugiat nulla pariatur. Excepteur sint occaecat cupidatat non proident, sunt in cur sint occaecatlpa qui officia.</p>
</div>
<div class="btn" style="left:611px;top:1185px;width:141px;height:49px">LEARN MORE</div>

<section class="abs featured-bg"></section>
<h2 class="abs h-title" style="left:0;width:1200px;text-align:center;top:1456px;font-size:35px">FEATURED <span class="accent">ITEMS</span></h2>

<h3 class="abs product-title" style="left:110px;top:1608px">PRODUCT NAME HERE</h3>
<p class="abs para" style="left:111px;top:1662px;width:420px">Lorem ipsum dolor sit amet, consectetur adipiscing elit, sed do eiusmod tempor incididunt ut labore et dolore magna aliqua. Ut enim ad minim veniam, quis nostrud exercitation ullamco laboris nisi ut aliquip ex ea commodoa.</p>
<div class="btn" style="left:111px;top:1797px;width:141px;height:48px">VIEW DETAILS</div>
<div class="photo" style="left:700px;top:1547px;width:389px;height:279px;background:linear-gradient(120deg,#e2e6ea,#c8ccd0 60%,#8d9096)" role="img" aria-label="Photo of a patient on a hospital bed wearing socks"></div>
<div class="photo framed" style="left:600px;top:1727px;width:201px;height:190px;background:linear-gradient(180deg,#f7f7f7,#eeeeee)" role="img" aria-label="Product photo of black thigh-high compression stockings"></div>

<div class="photo" style="left:111px;top:1917px;width:389px;height:278px;background:linear-gradient(100deg,#9ba6b0,#d8dde2 55%,#8fa6b3)" role="img" aria-label="Photo of a woman sitting by a window in knit socks"></div>
<div class="photo framed" style="left:398px;top:2097px;width:202px;height:190px;background:linear-gradient(180deg,#fbf7f4,#f1e5df)" role="img" aria-label="Product photo of beige knee-high compression socks"></div>
<h3 class="abs product-title" style="left:667px;top:1980px">PRODUCT NAME HERE</h3>
<p class="abs para" style="left:668px;top:2034px;width:421px">Lorem ipsum dolor sit amet, consectetur adipiscing elit, sed do eiusmod tempor incididunt ut labore et dolore magna aliqua. Ut enim ad minim veniam, quis nostrud exercitation ullamco laboris nisi ut aliquip ex ea commodoa.</p>
<div class="btn" style="left:668px;top:2168px;width:142px;height:50px">VIEW DETAILS</div>

<h3 class="abs product-title" style="left:110px;top:2344px">PRODUCT NAME HERE</h3>
<p class="abs para" style="left:111px;top:2398px;width:420px">Lorem ipsum dolor sit amet, consectetur adipiscing elit, sed do eiusmod tempor incididunt ut labore et dolore magna aliqua. Ut enim ad minim veniam, quis nostrud exercitation ullamco laboris nisi ut aliquip ex ea commodoa.</p>
<div class="btn" style="left:111px;top:2533px;width:141px;height:50px">VIEW DETAILS</div>
<div class="photo" style="left:700px;top:2284px;width:389px;height:278px;background:linear-gradient(120deg,#6f5a4c,#e6e2de 45%,#a89486)" role="img" aria-label="Photo of a woman putting on socks while sitting on a bed"></div>
<div class="photo framed" style="left:600px;top:2463px;width:201px;height:190px;background:linear-gradient(180deg,#f7f7f7,#eeeeee)" role="img" aria-label="Product photo of black knee-high compression socks"></div>

<section class="abs benefit-photo" role="img" aria-label="Photo of feet in white and pink cable-knit socks"></section>
<section class="abs benefit-panel"></section>
<h2 class="abs h-title" style="left:673px;top:2770px;font-size:35px;color:var(--white)"><span class="accent">OUR</span> BENEFITS</h2>
<div class="abs para on-dark" style="left:673px;top:2838px;width:415px">
  <p>Lorem ipsum dolor sit amet, consectetur adipiscing elit, sed do eiusmod tempor incididunt ut labore et dolore magna aliqua. Ut enim ad minim veniam, quis nostrud exercitation ullamco laboris nisi ut aliquip ex ea commodo consequat. Duis aute irure dolor in reprehenderit in voluptate velit esse cilluma.</p>
  <p style="margin-top:23px">Quis nostrud exercitation ullamco laboris nisi ut aliquip ex ea commodo consequat. Duis aute irure dolor in reprehenderit in voluptate velit esse cilluma.</p>
</div>
<div class="btn" style="left:673px;top:3097px;width:141px;height:49px">LEARN MORE</div>

<h2 class="abs h-title" style="left:0;width:1200px;text-align:center;top:3283px;font-size:35px"><span class="accent">OUR</span> SUPPLIERS</h2>
<svg class="abs" style="left:50px;top:3385px" width="16" height="28" viewBox="0 0 16 28"><path d="M14 2L3 14l11 12" stroke="#bbbbbb" stroke-width="2.5" fill="none"/></svg>
<svg class="abs" style="left:1132px;top:3385px" width="16" height="28" viewBox="0 0 16 28"><path d="M2 2l11 12L2 26" stroke="#222222" stroke-width="2.5" fill="none"/></svg>
<div class="supplier" style="left:111px"><span></span></div>
<div class="supplier" style="left:310px"><span></span></div>
<div class="supplier" style="left:509px"><span></span></div>
<div class="supplier" style="left:708px"><span></span></div>
<div class="supplier" style="left:907px"><span></span></div>

<footer class="abs footer"></footer>
<section class="abs newsletter">
  <h2 class="news-title">Subscribe Our Newsletter</h2>
  <p class="news-sub">Join our mailing list to receive the latest news and updates from our team</p>
  <div class="news-form"><div class="news-input">Emaill Address</div><div class="news-btn">SUBSCRIBE</div></div>
</section>

<div class="abs brand foot-brand" style="left:111px;top:3800px"><span class="brand-dot"></span>FLORN TECH</div>
<span class="social-round" style="left:148px"></span>
<span class="social-round ghost" style="left:191px"></span>
<span class="social-round ghost" style="left:233px"></span>
<span class="social-round ghost" style="left:276px"></span>

<div class="abs foot-col" style="left:450px;top:3790px">
  <h4>Quick Links</h4>
  <ul>
    <li><svg width="13" height="13" viewBox="0 0 14 14"><circle cx="7" cy="7" r="7" fill="#fcc30d"/><path d="M4 7h6M7.5 4.5L10 7 7.5 9.5" stroke="#262626" stroke-width="1.6" fill="none"/></svg>Home</li>
    <li><svg width="13" height="13" viewBox="0 0 14 14"><circle cx="7" cy="7" r="7" fill="#fcc30d"/><path d="M4 7h6M7.5 4.5L10 7 7.5 9.5" stroke="#262626" stroke-width="1.6" fill="none"/></svg>About Us</li>
    <li><svg width="13" height="13" viewBox="0 0 14 14"><circle cx="7" cy="7" r="7" fill="#fcc30d"/><path d="M4 7h6M7.5 4.5L10 7 7.5 9.5" stroke="#262626" stroke-width="1.6" fill="none"/></svg>Our Collections</li>
    <li><svg width="13" height="13" viewBox="0 0 14 14"><circle cx="7" cy="7" r="7" fill="#fcc30d"/><path d="M4 7h6M7.5 4.5L10 7 7.5 9.5" stroke="#262626" stroke-width="1.6" fill="none"/></svg>Suppliers</li>
    <li><svg width="13" height="13" viewBox="0 0 14 14"><circle cx="7" cy="7" r="7" fill="#fcc30d"/><path d="M4 7h6M7.5 4.5L10 7 7.5 9.5" stroke="#262626" stroke-width="1.6" fill="none"/></svg>Blog</li>
    <li><svg width="13" height="13" viewBox="0 0 14 14"><circle cx="7" cy="7" r="7" fill="#fcc30d"/><path d="M4 7h6M7.5 4.5L10 7 7.5 9.5" stroke="#262626" stroke-width="1.6" fill="none"/></svg>Contact Us</li>
  </ul>
</div>
<div class="abs foot-col" style="left:681px;top:3790px">
  <h4>Other Links</h4>
  <ul>
    <li><svg width="13" height="13" viewBox="0 0 14 14"><circle cx="7" cy="7" r="7" fill="#fcc30d"/><path d="M4 7h6M7.5 4.5L10 7 7.5 9.5" stroke="#262626" stroke-width="1.6" fill="none"/></svg>Site Map</li>
    <li><svg width="13" height="13" viewBox="0 0 14 14"><circle cx="7" cy="7" r="7" fill="#fcc30d"/><path d="M4 7h6M7.5 4.5L10 7 7.5 9.5" stroke="#262626" stroke-width="1.6" fill="none"/></svg>Privacy Policy</li>
    <li><svg width="13" height="13" viewBox="0 0 14 14"><circle cx="7" cy="7" r="7" fill="#fcc30d"/><path d="M4 7h6M7.5 4.5L10 7 7.5 9.5" stroke="#262626" stroke-width="1.6" fill="none"/></svg>Terms Of Use</li>
    <li><svg width="13" height="13" viewBox="0 0 14 14"><circle cx="7" cy="7" r="7" fill="#fcc30d"/><path d="M4 7h6M7.5 4.5L10 7 7.5 9.5" stroke="#262626" stroke-width="1.6" fill="none"/></svg>Legal Support</li>
  </ul>
</div>
<div class="abs foot-col" style="left:912px;top:3790px">
  <h4>Contact Us</h4>
  <ul>
    <li><svg width="13" height="14" viewBox="0 0 12 16"><path d="M6 0a6 6 0 016 6c0 4.5-6 10-6 10S0 10.5 0 6a6 6 0 016-6z" fill="#fcc30d"/><circle cx="6" cy="6" r="2.2" fill="#262626"/></svg><span>218, Maple Crest Rd,<br>United States</span></li>
    <li style="margin-top:8px"><svg width="13" height="13" viewBox="0 0 24 24"><path d="M6.6 10.8a15 15 0 006.6 6.6l2.2-2.2a1 1 0 011-.25 11.4 11.4 0 003.6.57 1 1 0 011 1V20a1 1 0 01-1 1A17 17 0 013 4a1 1 0 011-1h3.5a1 1 0 011 1c0 1.25.2 2.45.57 3.57a1 1 0 01-.25 1z" fill="#fcc30d"/></svg>555-014-2738</li>
    <li><svg width="14" height="11" viewBox="0 0 24 18"><rect x="1" y="1" width="22" height="16" rx="2" fill="#fcc30d"/><path d="M2 2l10 8 10-8" stroke="#262626" stroke-width="2" fill="none"/></svg>info@florntech.com</li>
  </ul>
</div>

<div class="abs divider"></div>
<p class="abs copyright">© 2021 Company Name. All Rights Reserved</p>

</body>
</html>
```